Clean and sophisticated website for Darulnoor

Darulnoor is a group of enthusiasts offering education, welfare, health and publications. The organization is going through a re branding phase and looking to design a new website for darulnoor.org. The current landing page will be replaced by the new website. Looking for a creative design that could be converted into a responsive wordpress theme and integrated on the website.

The new website will have all the content of the 4 different sites that are accessible from the landing page.

Target Market(s)

Donors, information seekers, and students.

Industry/Entity Type

Non-Profit

Number of Pages Required

5+ page

Font styles to use
Sans Serif

Requirements
Must have
• Sophisticated look.
• Multi lingual interface (English + Urdu)
• Great User experience and Easy Navigation
• SEO friendly
• Prominent sections for 4 main categories
• Responsive design
Nice to have
• banners
• Parallax
• Call to action buttons
• simple clean design
Should not have
• Dark Colors
• Busy portal style look
• Flash
• cluttered design

```html
<!DOCTYPE html>
<html lang="en">
<head>
<meta charset="utf-8">
<title>Darulnoor</title>
<link href="https://fonts.googleapis.com/css2?family=Oswald:wght@300;400;500&family=Open+Sans:wght@400;600;700&family=Noto+Naskh+Arabic:wght@400&display=swap" rel="stylesheet">
<style>
:root{
  --blue:#1f6fc4;
  --green:#3aaa48;
  --orange:#ef5a24;
  --red:#d8282f;
  --cyan:#1fa4dc;
  --fb:#2f5ea8;
  --ink:#2f2f2f;
  --muted:#666;
  --grey:#f1f1f1;
  --card:#f4f4f4;
  --dark:#2a2a2a;
}
*{box-sizing:border-box;margin:0;padding:0}
html,body{width:1200px;height:4157px;overflow:hidden}
body{font-family:"Open Sans",Arial,sans-serif;color:var(--ink);background:#fff;position:relative}
.wrap{width:1134px;margin:0 auto;position:relative}

/* header */
.site-header{height:192px;position:relative}
.brand-word{position:absolute;left:33px;top:62px;font-family:"Oswald",sans-serif;font-weight:400;font-size:70px;letter-spacing:8px;color:#3a3a3a;line-height:1}
.brand-mark{position:absolute;left:528px;top:18px;width:144px;text-align:center}
.brand-mark .square{width:84px;height:84px;background:var(--green);margin:0 auto 10px}
.brand-mark .name{font-weight:600;font-size:16px;letter-spacing:2px;color:#3a3a3a}
.brand-urdu{position:absolute;right:36px;top:44px;font-family:"Noto Naskh Arabic",serif;font-size:78px;color:#444;line-height:1.2;direction:rtl}

/* nav */
.main-nav{height:64px;background:#fff}
.main-nav .bar{height:52px;background:var(--blue);padding-left:33px;display:flex}
.main-nav .line{height:5px;background:var(--green);margin-top:4px}
.main-nav a{color:#fff;text-decoration:none;font-size:13px;font-weight:700;padding:0 34px;line-height:52px;letter-spacing:.5px}
.main-nav a.active{background:var(--green)}

/* hero */
.hero{height:564px;padding-top:21px}
.hero-box{position:relative;width:1134px;height:532px;margin:0 auto;background:linear-gradient(180deg,#05070c 0%,#101722 45%,#3a3a2c 78%,#1b2416 100%);overflow:hidden}
.hero-box .glow{position:absolute;left:330px;top:150px;width:760px;height:300px;background:radial-gradient(ellipse at center,rgba(235,200,120,.55),rgba(120,110,70,.2) 55%,transparent 75%)}
.hero-text{position:absolute;left:40px;top:60px;color:#fff}
.hero-text h1{font-family:"Oswald",sans-serif;font-weight:400;font-size:46px;letter-spacing:1px;line-height:1}
.hero-text p{font-size:15px;line-height:1.55;margin-top:16px;width:440px}
.namaz{position:absolute;left:0;bottom:0;width:100%;height:60px;background:rgba(0,0,0,.55);color:#fff;display:flex;align-items:center;padding-left:30px}
.namaz h3{font-family:"Oswald",sans-serif;font-weight:400;font-size:25px;margin-right:46px}
.namaz span{font-size:13px;margin-right:22px}
.namaz .sep{opacity:.7}

/* categories */
.categories{height:390px;padding-top:20px}
.cat-grid{display:flex;gap:33px;width:1134px;margin:0 auto}
.cat-card{width:258px;height:355px;background:var(--card)}
.cat-card .photo{height:175px}
.cat-card .body{padding:20px 26px}
.cat-card h3{font-size:19px;font-weight:700;letter-spacing:.5px;padding-bottom:8px;border-bottom:3px solid var(--blue);width:205px}
.cat-card.welfare h3,.cat-card.publications h3{border-color:var(--orange)}
.cat-card.education h3{border-color:#555}
.cat-card p{font-size:13px;color:var(--muted);line-height:1.6;margin-top:14px}
.cat-card .more{display:block;font-size:11px;font-weight:700;color:var(--blue);margin-top:10px}
.welfare .more,.publications .more{color:var(--orange)}
.education .more{color:#555}

/* social band */
.social-band{height:146px;position:relative;overflow:hidden}
.social-band .seg{position:absolute;top:4px;height:138px;display:flex;align-items:center;padding-left:60px;color:#fff;font-size:14px;font-weight:600}
.seg .dot{width:40px;height:40px;border-radius:50%;background:rgba(255,255,255,.9);margin-right:16px;flex:none}
.seg .pill{background:rgba(0,0,0,.22);border-radius:20px;padding:11px 18px 11px 14px;display:flex;align-items:center}
.seg .pill .dot{width:28px;height:28px;margin-right:12px}
.seg.friendbook{left:0;width:330px;background:var(--fb);clip-path:polygon(0 0,100% 0,88% 100%,0 100%);padding-left:40px}
.seg.viewtube{left:270px;width:360px;background:var(--red);clip-path:polygon(12% 0,100% 0,88% 100%,0 100%)}
.seg.chirper{left:570px;width:360px;background:var(--cyan);clip-path:polygon(12% 0,100% 0,88% 100%,0 100%)}
.seg.chatline{left:870px;width:330px;background:var(--green);clip-path:polygon(13% 0,100% 0,100% 100%,0 100%)}
.spacer{height:24px}

/* mission */
.mission{height:430px;background:var(--grey);position:relative}
.mission .text{position:absolute;left:55px;top:58px;width:500px}
.mission h2{font-weight:400;font-size:45px;color:#333}
.mission ul{list-style:none;margin-top:28px}
.mission li{font-size:15px;line-height:2;padding-left:32px;position:relative}
.mission li::before{content:"";position:absolute;left:2px;top:11px;width:7px;height:7px;border-right:2px solid var(--red);border-top:2px solid var(--red);transform:rotate(45deg)}
.mission p{font-size:13px;color:var(--muted);line-height:1.7;margin-top:38px;width:480px}
.mission .photo{position:absolute;left:610px;top:0;width:590px;height:395px;background:linear-gradient(180deg,#9aaebf 0%,#c9c4b3 45%,#b48a5a 70%,#8c6a44 100%)}

/* recent */
.recent{height:630px;padding-top:45px}
.section-title{text-align:center;font-weight:400;font-size:40px;color:#333}
.act-grid{display:flex;gap:50px;width:1134px;margin:38px auto 0}
.act-card{width:345px}
.act-card .photo{height:190px}
.act-card h3{font-size:18px;font-weight:700;margin-top:28px;letter-spacing:.3px}
.act-card h4{font-size:15px;font-weight:600;color:#444;padding-bottom:8px;border-bottom:3px solid var(--blue);width:335px}
.act-card.masjid h4{border-color:var(--orange)}
.act-card.ambulance h4{border-color:var(--green)}
.act-card p{font-size:13px;color:var(--muted);line-height:1.65;margin-top:16px;height:110px}
.act-card .more{font-size:11px;font-weight:700;color:var(--red);margin-top:22px;display:block}

/* membership */
.membership{height:260px;padding-top:15px}
.membership .band{height:238px;background:var(--grey);position:relative}
.membership h2{position:absolute;left:40px;top:80px;font-weight:400;font-size:45px;color:#333}
.membership .sub{position:absolute;left:40px;top:142px;font-size:16px;font-weight:600;color:#444}
.membership svg{position:absolute;left:570px;top:0}

/* gallery */
.gallery{height:740px;padding-top:55px}
.gal-grid{display:flex;gap:33px;width:1134px;margin:32px auto 0}
.gal-card{width:258px;height:580px;background:var(--card)}
.gal-card .photo{height:168px}
.gal-card .date{height:52px;display:flex;justify-content:space-between;align-items:center;padding:0 26px;border-bottom:3px solid #333;margin:0 0 0}
.gal-card .date span{font-size:20px;font-weight:700}
.gal-card p{font-size:13px;color:var(--muted);line-height:1.72;padding:14px 28px}

/* banner */
.banner{height:400px;position:relative;overflow:hidden;background:linear-gradient(120deg,#2c1608 0%,#5c2a0c 30%,#1b4a2c 55%,#3a2a10 70%)}
.banner .pattern{position:absolute;left:0;top:0;width:760px;height:400px;background:radial-gradient(ellipse at 55% 60%,rgba(255,170,40,.55),transparent 60%)}
.banner .photo-a{position:absolute;left:600px;top:0;width:430px;height:400px;background:linear-gradient(180deg,#7fa2c9,#c9b39a 60%,#9a6d44);clip-path:polygon(32% 0,100% 0,68% 100%,0 100%)}
.banner .photo-b{position:absolute;left:880px;top:0;width:320px;height:400px;background:linear-gradient(180deg,#d6c2a5,#a5683c 70%,#7d4322);clip-path:polygon(40% 0,100% 0,100% 100%,0 100%)}
.banner .cut{position:absolute;left:600px;bottom:0;width:600px;height:400px;background:#fff;clip-path:polygon(86% 0,100% 0,100% 0,60% 100%,55% 100%)}
.banner .copy{position:absolute;left:34px;top:48px;color:#fff;font-size:31px;line-height:1.3;letter-spacing:.5px}
.banner .copy b{font-weight:700}
.banner .copy .hl{color:#ff7a1a;font-weight:700}

/* footer */
.site-footer{height:317px;position:relative;background:#fff}
.foot-brand{position:absolute;left:58px;top:60px;width:120px;text-align:center}
.foot-brand .square{width:82px;height:82px;background:var(--green);margin:0 auto 10px}
.foot-brand .name{font-size:13px;font-weight:600;letter-spacing:1px;color:#3a3a3a}
.foot-col{position:absolute;top:62px}
.foot-col h4{font-size:15px;font-weight:700;letter-spacing:.5px;margin-bottom:18px}
.foot-col p,.foot-col li{font-size:12px;color:var(--muted);line-height:1.7}
.foot-col ul{list-style:none}
.foot-col li{display:flex;align-items:center;gap:8px}
.foot-col li svg{flex:none}
.loc{left:258px}
.mail{left:556px;width:250px}
.follow{left:910px}
.subscribe{display:flex;margin-top:22px}
.subscribe .field{width:150px;height:36px;border:1px solid #ccc;font-size:11px;color:#aaa;padding:10px}
.subscribe .btn{height:36px;background:var(--green);color:#fff;font-size:13px;font-weight:600;padding:9px 12px}
.icons{display:flex;gap:10px}
.icons span{width:30px;height:30px;border-radius:50%;background:#777}
</style>
</head>
<body>

<header class="site-header">
  <div class="brand-word">DARULNOOR</div>
  <div class="brand-mark"><div class="square"></div><div class="name">DARULNOOR</div></div>
  <div class="brand-urdu">دار النور</div>
</header>

<nav class="main-nav">
  <div class="bar">
    <a class="active">HOME</a><a>ABOUT US</a><a>PUBLICATIONS</a><a>WELFARE</a><a>EDUCATION</a><a>BAYANAT</a><a>CONTACT US</a>
  </div>
  <div class="line"></div>
</nav>

<section class="hero">
  <div class="hero-box" role="img" aria-label="Campus buildings and minarets lit up at night">
    <div class="glow"></div>
    <div class="hero-text">
      <h1>WE BUILT AROUND MENTORSHIP</h1>
      <p>A group of like minded consectetur adipiscing elit. Respondent extrema primis, media utrisque, omnia omnibus.</p>
    </div>
    <div class="namaz">
      <h3>Namaz Timing</h3>
      <span>Fajar (6:25)</span><span class="sep">—</span><span>Zahur (1:30)</span><span class="sep">—</span><span>Asar (4:30)</span><span class="sep">—</span><span>Magrib (Sunset)</span><span class="sep">—</span><span>Isha (7:30)</span><span class="sep">—</span><span>Jumma (1:30)</span>
    </div>
  </div>
</section>

<section class="categories">
  <div class="cat-grid">
    <article class="cat-card bayanat">
      <div class="photo" role="img" aria-label="Prayer hall interior with carpet" style="background:linear-gradient(180deg,#8a5a34,#c98b4a 60%,#7a2f22)"></div>
      <div class="body"><h3>BAYANAT</h3><p>Ifadat ul Awwal Mohabbat<br>ka Paigham</p><span class="more">LEARN MORE &gt;</span></div>
    </article>
    <article class="cat-card welfare">
      <div class="photo" role="img" aria-label="White ambulance van parked outside" style="background:linear-gradient(180deg,#6e7f8f,#d9dde2 50%,#8a8a86)"></div>
      <div class="body"><h3>WELFARE</h3><p>Bank Transfer<br>Send us Cheque</p><span class="more">LEARN MORE &gt;</span></div>
    </article>
    <article class="cat-card publications">
      <div class="photo" role="img" aria-label="Institute building block" style="background:linear-gradient(180deg,#9fb4c8,#b99a7c 55%,#8c6d55)"></div>
      <div class="body"><h3>PUBLICATIONS</h3><p>Noor-e-Fikr<br>Intellect Magazine</p><span class="more">LEARN MORE &gt;</span></div>
    </article>
    <article class="cat-card education">
      <div class="photo" role="img" aria-label="Classroom with desks" style="background:linear-gradient(180deg,#d8d2c6,#a89682 60%,#6f5c4a)"></div>
      <div class="body"><h3>EDUCATION</h3><p>Bright Path Institute<br>Jamia Darulnoor</p><span class="more">LEARN MORE &gt;</span></div>
    </article>
  </div>
</section>

<section class="social-band">
  <div class="seg friendbook"><div class="pill"><span class="dot"></span>Like us on Friendbook</div></div>
  <div class="seg viewtube"><div class="pill"><span class="dot"></span>Subscribe us on ViewTube</div></div>
  <div class="seg chirper"><div class="pill"><span class="dot"></span>Follow us on Chirper</div></div>
  <div class="seg chatline"><div class="pill"><span class="dot"></span>ChatLine Subscribe Online</div></div>
</section>
<div class="spacer"></div>

<section class="mission">
  <div class="text">
    <h2>Our Mission &amp; Believes</h2>
    <ul>
      <li>Our model is built around mentorship</li>
      <li>We create network</li>
      <li>We bring in experts to teach the real building blocks</li>
      <li>We cultivate a creative</li>
    </ul>
    <p>Integer sit amet augue iaculis, ultricies justo nec, commodo nisl. Class aptent taciti sociosqu ad litora torquent per conubia nostra.</p>
  </div>
  <div class="photo" role="img" aria-label="Mosque with twin minarets under a cloudy sky"></div>
</section>

<section class="recent">
  <h2 class="section-title">Recent Activities</h2>
  <div class="act-grid">
    <article class="act-card food">
      <div class="photo" role="img" aria-label="Dining hall with low seating" style="background:linear-gradient(180deg,#c9b08e,#a07a55 50%,#8a2c20)"></div>
      <h3>FOOD SERVICES</h3><h4>Meals in Education Centers</h4>
      <p>The Trust provides free of cost breakfast, lunch and dinner to students and faculty members in its 2 main campuses located in Karachi, Sindh and Chakwal, Punjab. The Karachi campus currently houses approximately 500 students...</p>
      <span class="more">READ MORE &gt;</span>
    </article>
    <article class="act-card masjid">
      <div class="photo" role="img" aria-label="Masjid with minaret and courtyard" style="background:linear-gradient(180deg,#86a8cc,#c8c0aa 55%,#8a7a55)"></div>
      <h3>MASJID &amp; QURANIC INSTITUTES</h3><h4>These centers which includes</h4>
      <p>These education centers are used as focal point for other welfare initiatives in adjoining areas such as distribution of food, Sehri and Iftar in the month of Ramadan, digging of wells and extension of water supply lines in areas deprived of these necessities.</p>
      <span class="more">READ MORE &gt;</span>
    </article>
    <article class="act-card ambulance">
      <div class="photo" role="img" aria-label="Ambulance van on the road" style="background:linear-gradient(180deg,#b5c2cf,#ecedee 50%,#9a9a96)"></div>
      <h3>AMBULANCE SERVICE</h3><h4>These services includes</h4>
      <p>DWT has recently launched its Ambulance service for all areas of Karachi. Imported vehicles are being used as ambulances and specifically fabricated with all the necessary equipment for dealing with any emergency situation.</p>
      <span class="more">READ MORE &gt;</span>
    </article>
  </div>
</section>

<section class="membership">
  <div class="band">
    <h2>Life Time Membership</h2>
    <div class="sub">Receiving, Gratitude, and Generosity all grow together.</div>
    <svg width="600" height="238" viewBox="0 0 600 238" font-family="Open Sans, sans-serif">
      <g fill="#fff" stroke="#ef5a24" stroke-width="3">
        <circle cx="42" cy="40" r="26"/><circle cx="72" cy="118" r="26"/><circle cx="42" cy="196" r="26"/>
        <circle cx="442" cy="118" r="28"/>
      </g>
      <g font-size="12" text-anchor="middle" fill="#333">
        <text x="42" y="44">1000</text><text x="72" y="122">1000</text><text x="42" y="200">1000</text>
      </g>
      <text x="442" y="124" font-size="17" text-anchor="middle" fill="#333">1</text>
      <polygon points="110,45 290,45 330,118 290,191 110,191 150,118" fill="none" stroke="#ef5a24" stroke-width="3"/>
      <text x="232" y="78" font-size="15" text-anchor="middle" fill="#333">Rs. 12000/m</text>
      <path d="M232 88 V150 M224 96 L232 88 L240 96 M224 142 L232 150 L240 142" stroke="#333" stroke-width="2" fill="none"/>
      <text x="232" y="172" font-size="15" text-anchor="middle" fill="#333">12 Members</text>
      <text x="370" y="132" font-size="38" text-anchor="middle" fill="#333">=</text>
      <text x="482" y="123" font-size="15" fill="#333">Quranic Institute</text>
    </svg>
  </div>
</section>

<section class="gallery">
  <h2 class="section-title">Gallery</h2>
  <div class="gal-grid">
    <article class="gal-card">
      <div class="photo" role="img" aria-label="Corridor with arches" style="background:linear-gradient(180deg,#d7d0c2,#a5947c 60%,#6b5a48)"></div>
      <div class="date"><span>MAY 2011</span><svg width="22" height="22" viewBox="0 0 22 22"><rect x="2" y="4" width="18" height="16" fill="#333"/><rect x="4" y="9" width="14" height="9" fill="#fff"/><rect x="6" y="1" width="3" height="5" fill="#333"/><rect x="13" y="1" width="3" height="5" fill="#333"/></svg></div>
      <p>Darulnoor Trust made an effort to help out those under privileged families who are unable to get their daughters married off because of lack of provisions for dowry. Darulnoor Trust distributed valuables clothes amongst 110 girls of 8 small villages in the Port Qasim area in an effort to help build their dowry.</p>
    </article>
    <article class="gal-card">
      <div class="photo" role="img" aria-label="Lit prayer hall at evening" style="background:linear-gradient(180deg,#3a2410,#b07a2e 55%,#5a3a18)"></div>
      <div class="date"><span>JANUARY 2011</span><svg width="22" height="22" viewBox="0 0 22 22"><rect x="2" y="4" width="18" height="16" fill="#333"/><rect x="4" y="9" width="14" height="9" fill="#fff"/><rect x="6" y="1" width="3" height="5" fill="#333"/><rect x="13" y="1" width="3" height="5" fill="#333"/></svg></div>
      <p>Under the supervision of Darulnoor Trust, the students of its quranic institutes were assessed on their learnings for the first time in January, 2011 to judge where the stood. Alhamdulillah, with the help of these institutes the students have learned to recite the Quran with proper Tajweed and have increased their knowledge.</p>
    </article>
    <article class="gal-card">
      <div class="photo" role="img" aria-label="Minarets rising above trees" style="background:linear-gradient(180deg,#9cb6cf,#c4c7bd 55%,#5e7048)"></div>
      <div class="date"><span>OCTOBER 2010</span><svg width="22" height="22" viewBox="0 0 22 22"><rect x="2" y="4" width="18" height="16" fill="#333"/><rect x="4" y="9" width="14" height="9" fill="#fff"/><rect x="6" y="1" width="3" height="5" fill="#333"/><rect x="13" y="1" width="3" height="5" fill="#333"/></svg></div>
      <p>Darulnoor Trust has undertaken to build shelter homes for the flood affected families in Noorabad on an 80 acre piece of vast land. It will accommodate 5000 affected families and their food provisions will also be taken care of.</p>
    </article>
    <article class="gal-card">
      <div class="photo" role="img" aria-label="Campus building lit at night" style="background:linear-gradient(180deg,#0d1420,#4a5240 55%,#2a3320)"></div>
      <div class="date"><span>SEPTEMBER 2010</span><svg width="22" height="22" viewBox="0 0 22 22"><rect x="2" y="4" width="18" height="16" fill="#333"/><rect x="4" y="9" width="14" height="9" fill="#fff"/><rect x="6" y="1" width="3" height="5" fill="#333"/><rect x="13" y="1" width="3" height="5" fill="#333"/></svg></div>
      <p>In the blessed month of Ramadan, 2010, Jamia Darulnoor Welfare Trust distributed Iftaar packages to many small hamlets. In 6 hamlets they distributed Iftaar comprising of dates and various fruits, amongst other items, to almost 110 families.</p>
    </article>
  </div>
</section>

<section class="banner" role="img" aria-label="Stained glass light and mosque courtyard photographs">
  <div class="pattern"></div>
  <div class="photo-a"></div>
  <div class="photo-b"></div>
  <div class="copy">WE BRING IN <span class="hl">EXPERTS</span> TO TEACH<br>THE <b>REAL</b> BUILDING BLOCKS</div>
</section>

<footer class="site-footer">
  <div class="foot-brand"><div class="square"></div><div class="name">DARULNOOR</div></div>
  <div class="foot-col loc">
    <h4>OUR LOCATION</h4>
    <ul>
      <li><svg width="10" height="14" viewBox="0 0 10 14"><path d="M5 0a5 5 0 0 1 5 5c0 4-5 9-5 9S0 9 0 5a5 5 0 0 1 5-5z" fill="#777"/><circle cx="5" cy="5" r="2" fill="#fff"/></svg>123 W Main Street</li>
      <li style="padding-left:18px">West Area, IL 12345</li>
      <li style="margin-top:10px"><svg width="10" height="12" viewBox="0 0 10 12"><rect x="1" y="0" width="8" height="12" rx="1.5" fill="#777"/></svg>Phone: 123-456-7890</li>
      <li style="padding-left:18px">www.darulnoor.org</li>
      <li><svg width="12" height="9" viewBox="0 0 12 9"><rect width="12" height="9" fill="#777"/><path d="M0 0 L6 5 L12 0" stroke="#fff" fill="none"/></svg>Email: info@darulnoor.org</li>
    </ul>
  </div>
  <div class="foot-col mail">
    <h4>JOIN OUR MAILING LIST</h4>
    <p>Your about us information would fit here nicely</p>
    <div class="subscribe"><div class="field">Email address</div><div class="btn">Submit</div></div>
  </div>
  <div class="foot-col follow">
    <h4>FOLLOW US OUT THERE</h4>
    <div class="icons"><span></span><span></span><span></span><span></span></div>
  </div>
</footer>

</body>
</html>
```